I need the following on my business card:
- Name: Dana Whitcomb
- License # 0M93216
- Title: Producer
- Phone: (555) 017-3904
- Email: Dana@CorbelInsuranceServices.com

- Company: Corbel Insurance Services
- Address: 27408 Larkmoor Ave Suite 610, Sherman Oaks, CA 90217
- Website: www.CorbelInsuranceServices.com

Also add our slogan on the card: "Where Trust Meets Coverage"

```html
<!DOCTYPE html>
<html lang="en">
<head>
<meta charset="utf-8">
<title>Corbel Insurance Services – Business Card</title>
<link rel="stylesheet" href="https://fonts.googleapis.com/css2?family=Poppins:wght@400;500;600;700&display=swap">
<style>
  :root {
    --navy: #263271;
    --green: #17984a;
    --grey: #6b6b6b;
    --paper: #ffffff;
    --backdrop: #e9e9e9;
  }
  * { box-sizing: border-box; margin: 0; padding: 0; }
  html, body {
    width: 1200px;
    height: 2345px;
    overflow: hidden;
    background: var(--backdrop);
    font-family: "Poppins", sans-serif;
  }
  .sheet {
    position: relative;
    width: 1200px;
    height: 2345px;
    display: flex;
    flex-direction: column;
    align-items: center;
    justify-content: center;
    gap: 40px;
  }
  .card {
    position: relative;
    width: 960px;
    height: 548px;
    background: var(--paper);
    box-shadow: 0 18px 30px -18px rgba(0,0,0,0.25);
    overflow: hidden;
  }
  .card__band {
    position: absolute;
    left: 0; right: 0; bottom: 0;
    height: 64px;
    background: var(--navy);
    color: #fff;
    display: flex;
    align-items: center;
    justify-content: center;
    font-weight: 500;
  }

  /* Front */
  .brand {
    display: flex;
    align-items: center;
    gap: 14px;
    color: var(--navy);
    font-weight: 600;
  }
  .brand__square {
    background: var(--green);
    flex: none;
  }
  .card--front .brand {
    position: absolute;
    left: 50%;
    top: 236px;
    transform: translate(-50%, -50%);
    font-size: 46px;
    letter-spacing: 0.5px;
    white-space: nowrap;
  }
  .card--front .brand__square { width: 30px; height: 30px; }
  .slogan {
    font-size: 21px;
    letter-spacing: 6px;
    text-transform: uppercase;
    font-weight: 500;
  }

  /* Back */
  .card--back .brand {
    position: absolute;
    right: 48px;
    top: 58px;
    font-size: 22px;
    gap: 10px;
    white-space: nowrap;
  }
  .card--back .brand__square { width: 14px; height: 14px; }
  .divider {
    position: absolute;
    left: 0; right: 0;
    top: 152px;
    height: 4px;
    background: var(--green);
  }
  .person {
    position: absolute;
    left: 46px;
    top: 248px;
  }
  .person__name {
    font-size: 48px;
    font-weight: 600;
    color: var(--navy);
    line-height: 1.05;
  }
  .person__title {
    font-size: 27px;
    color: var(--grey);
    line-height: 1.1;
  }
  .contacts {
    position: absolute;
    left: 450px;
    top: 228px;
    list-style: none;
  }
  .contacts__item {
    display: flex;
    align-items: center;
    gap: 16px;
    height: 50px;
    font-size: 21px;
    font-weight: 500;
    color: var(--navy);
  }
  .contacts__icon { width: 26px; height: 26px; flex: none; }
  .license {
    position: absolute;
    left: 450px;
    top: 420px;
    font-size: 17px;
    color: var(--grey);
    letter-spacing: 1px;
  }
  .address {
    font-size: 21px;
    letter-spacing: 2px;
  }
</style>
</head>
<body>
<main class="sheet">

  <section class="card card--front">
    <div class="brand">
      <span class="brand__square"></span>
      <span class="brand__name">Corbel Insurance Services</span>
    </div>
    <div class="card__band"><p class="slogan">Where Trust Meets Coverage</p></div>
  </section>

  <section class="card card--back">
    <div class="brand">
      <span class="brand__square"></span>
      <span class="brand__name">Corbel Insurance Services</span>
    </div>
    <div class="divider"></div>

    <div class="person">
      <h1 class="person__name">Dana Whitcomb</h1>
      <p class="person__title">Producer</p>
    </div>

    <ul class="contacts">
      <li class="contacts__item">
        <svg class="contacts__icon" viewBox="0 0 26 26" aria-hidden="true">
          <circle cx="13" cy="13" r="13" fill="#17984a"/>
          <path d="M9.2 7.5l2 2.6-1.2 1.4c.8 1.7 2 2.9 3.7 3.7l1.4-1.2 2.6 2-1 1.9c-4.3-.3-8-4-8.4-8.4z" fill="#fff"/>
        </svg>
        <span>(555) 017-3904</span>
      </li>
      <li class="contacts__item">
        <svg class="contacts__icon" viewBox="0 0 26 26" aria-hidden="true">
          <circle cx="13" cy="13" r="13" fill="#17984a"/>
          <rect x="7" y="9" width="12" height="8.5" rx="1" fill="#fff"/>
          <path d="M7.5 9.8l5.5 4 5.5-4" fill="none" stroke="#17984a" stroke-width="1.3"/>
        </svg>
        <span>Dana@CorbelInsuranceServices.com</span>
      </li>
      <li class="contacts__item">
        <svg class="contacts__icon" viewBox="0 0 26 26" aria-hidden="true">
          <circle cx="13" cy="13" r="13" fill="#17984a"/>
          <g fill="none" stroke="#fff" stroke-width="1.4">
            <circle cx="13" cy="13" r="6.5"/>
            <ellipse cx="13" cy="13" rx="3" ry="6.5"/>
            <path d="M6.5 13h13M7.5 9.8h11M7.5 16.2h11"/>
          </g>
        </svg>
        <span>www.CorbelInsuranceServices.com</span>
      </li>
    </ul>

    <p class="license">LICENSE #0M93216</p>

    <div class="card__band"><p class="address">27408 Larkmoor Ave Suite 610, Sherman Oaks, CA 90217</p></div>
  </section>

</main>
</body>
</html>
```